4K Business Card Design

We need a business card that emphasizes consulting services worldwide. The name of the company is KKKK Consulting Group. We provide consulting services across several industries including but not limited to commodities, telecom, manufacturing, logistics, marketing and operations. We would like to see a creative design that emphasizes the global aspect, including Latin America and US markets, as well the bilingual nature of the service offerings.

The contact information section should include icons to represent the following data:
1) Name, Title and Company Name
2) Mobile Number
3) Skype ID
4) Email
5) Web Page
6) Location

We would like to see a card that emphasizes the worldwide concept. The back of the card should be simple, including only the logo (or a portion of the logo) and the slogan.

We would also like to see business cards in a booklet format. The colors to be used should be the same combination of colors used in the logos attached to this brief.

The logo design and some business card examples from Artful Herd are attached for reference on style and look.

Target Market(s)

International business executives, 45-65 years of age, bilingual

Industry/Entity Type

Marketing

Colors
0792cd
34a7d8
85cae6
ffffff
cee9f5
ecf7fb

Requirements
Must have
• Please follow colors in logo attached.

2) Mobile Number
3) Skype ID
4) Email
5) Web Page
6) Location
Nice to have
• Global concept, consulting profile, diverse industry focus
Should not have
• No black color

```html
<!DOCTYPE html>
<html lang="en">
<head>
<meta charset="utf-8">
<title>KKKK Consulting Group – Business Card</title>
<link rel="stylesheet" href="https://fonts.googleapis.com/css2?family=Anton&family=Lobster+Two:ital,wght@1,700&family=Quicksand:wght@400;500&display=swap">
<style>
  :root {
    --blue-deep: #0792cd;
    --blue-mid: #34a7d8;
    --blue-soft: #85cae6;
    --blue-pale: #cee9f5;
    --blue-mist: #ecf7fb;
    --white: #ffffff;
    --label: #111418;
    --guide-trim: #27a6e0;
    --guide-bleed: #d6374a;
    --logo-grey: #5f8fa6;
  }
  * { margin: 0; padding: 0; box-sizing: border-box; }
  html, body { width: 851px; height: 1200px; overflow: hidden; background: var(--white); }
  .sheet {
    position: relative; width: 851px; height: 1200px;
    background: var(--white);
    border: 3px solid var(--label);
  }
  .side-label {
    position: absolute; left: 0; width: 100%; text-align: center;
    font-family: "Anton", sans-serif; font-size: 64px; letter-spacing: 2px;
    color: var(--label); line-height: 1;
  }
  .side-label--back { top: 50px; }
  .side-label--front { top: 1080px; }

  .card {
    position: absolute; left: 51px; width: 752px; height: 423px;
    background: linear-gradient(180deg, var(--white) 0%, var(--blue-mist) 100%);
    overflow: hidden;
  }
  .card--back { top: 160px; }
  .card--front { top: 641px; }
  .card svg.card-art { position: absolute; inset: 0; width: 100%; height: 100%; }

  .guide { position: absolute; pointer-events: none; }
  .guide--trim { border: 2px solid var(--guide-trim); }
  .guide--bleed { border: 2px solid var(--guide-bleed); }

  .holder-name {
    position: absolute; font-family: "Lobster Two", cursive;
    font-style: italic; font-weight: 700; color: var(--white); line-height: 1.2;
  }
  .holder-title {
    position: absolute; font-family: "Quicksand", sans-serif;
    font-weight: 500; color: var(--white); font-size: 14px; line-height: 1.2;
    white-space: nowrap;
  }

  .brand {
    position: absolute; display: flex; flex-direction: column; align-items: center;
    font-family: "Quicksand", sans-serif; font-weight: 500; color: var(--logo-grey);
    text-align: center;
  }
  .brand__mark { background: var(--blue-soft); }
  .brand__name { line-height: 1.05; letter-spacing: 1px; }

  .company {
    position: absolute; left: 360px; top: 138px;
    font-family: "Quicksand", sans-serif;
  }
  .company__name { font-size: 30px; font-weight: 500; color: var(--blue-deep); line-height: 1.15; }
  .company__city { font-size: 18px; color: var(--blue-soft); margin-top: 2px; }

  .contacts {
    position: absolute; left: 360px; top: 262px; list-style: none;
    font-family: "Quicksand", sans-serif; font-size: 18px; color: var(--blue-mid);
    line-height: 24px;
  }
</style>
</head>
<body>
<main class="sheet">

  <h2 class="side-label side-label--back">BACK</h2>

  <section class="card card--back" aria-label="Card back">
    <svg class="card-art" viewBox="0 0 752 423" preserveAspectRatio="none" aria-hidden="true">
      <defs>
        <linearGradient id="mist" x1="0" y1="0" x2="0" y2="1">
          <stop offset="0" stop-color="#ffffff"/>
          <stop offset="1" stop-color="#ecf7fb"/>
        </linearGradient>
      </defs>
      <rect x="0" y="0" width="752" height="423" fill="url(#mist)"/>
      <rect x="0" y="58" width="752" height="10" fill="var(--blue-pale)"/>
      <rect x="0" y="68" width="752" height="8" fill="var(--blue-soft)"/>
      <path d="M0 36 H290 Q308 36 316 54 L324 76 H0 Z" fill="var(--blue-soft)"/>
      <path d="M505 56 Q517 40 545 40 H752 V76 H490 Z" fill="var(--blue-deep)"/>
      <path d="M0 355 H752 V423 H0 Z" fill="var(--blue-soft)"/>
      <path d="M0 373 H752 V423 H0 Z" fill="var(--blue-deep)"/>
    </svg>
    <span class="holder-name" style="left:44px; top:38px; font-size:27px;">Lucia Fernandez</span>
    <span class="holder-title" style="right:70px; top:49px;">President &amp; CEO</span>

    <div class="brand" style="left:70px; top:118px; width:240px;">
      <span class="brand__mark" style="width:70px; height:70px; margin-bottom:12px;"></span>
      <span class="brand__name" style="font-size:29px;">4K Consulting<br>Group</span>
    </div>

    <div class="company">
      <p class="company__name">KKKK Consulting Group</p>
      <p class="company__city">Palm Harbor, FL</p>
    </div>
    <ul class="contacts">
      <li>Email: k4cg@mailbox.com</li>
      <li>Skype ID: k4consultinggroup</li>
      <li>Mobile: +1 305 555-0148</li>
    </ul>

    <div class="guide guide--bleed" style="left:28px; top:22px; right:28px; bottom:22px;"></div>
    <div class="guide guide--trim" style="left:8px; top:8px; right:8px; bottom:8px;"></div>
  </section>

  <section class="card card--front" aria-label="Card front">
    <svg class="card-art" viewBox="0 0 752 423" preserveAspectRatio="none" aria-hidden="true">
      <defs>
        <linearGradient id="mist2" x1="0" y1="0" x2="0" y2="1">
          <stop offset="0" stop-color="#ffffff"/>
          <stop offset="1" stop-color="#ecf7fb"/>
        </linearGradient>
      </defs>
      <rect x="0" y="0" width="752" height="423" fill="url(#mist2)"/>
      <rect x="0" y="318" width="752" height="105" fill="var(--blue-pale)"/>
      <rect x="0" y="335" width="752" height="88" fill="var(--blue-deep)"/>
      <path d="M180 335 Q186 290 226 290 H526 Q566 290 572 335 L578 372 Q580 384 566 384 H186 Q172 384 174 372 Z" fill="var(--blue-soft)"/>
    </svg>

    <div class="brand" style="left:226px; top:70px; width:300px;">
      <span class="brand__mark" style="width:84px; height:84px; margin-bottom:16px;"></span>
      <span class="brand__name" style="font-size:36px;">4K Consulting<br>Group</span>
    </div>

    <span class="holder-name" style="left:0; width:752px; text-align:center; top:310px; font-size:32px;">Lucia Fernandez</span>

    <div class="guide guide--bleed" style="left:10px; top:10px; right:10px; bottom:10px;"></div>
    <div class="guide guide--trim" style="left:28px; top:26px; right:28px; bottom:26px;"></div>
  </section>

  <h2 class="side-label side-label--front">FRONT</h2>

</main>
</body>
</html>
```